MORIVO VEGAN SUSHI

www.morivo-restaurant.de
We are open in 2018 and are an innovative restaurant from Munich. We would like a cool design for our drinks and food menu. It's very simple at the moment. See the File menu. In any case, our logo should appear. On the website we use neutraface as a font. But it's not a must. We are only open in the evening and appeal to a young, upscale audience.

```html
<!DOCTYPE html>
<html lang="de">
<head>
<meta charset="utf-8">
<title>Morivo – Speisekarte</title>
<link rel="stylesheet" href="https://fonts.googleapis.com/css2?family=Ubuntu:ital,wght@0,300;0,400;0,500;1,300&family=Stardos+Stencil:wght@700&display=swap">
<style>
  :root{
    --wood:#eceeee;
    --wood-line:#d9dcdc;
    --brand-red:#8c1a1d;
    --price-red:#9b1b1f;
    --ink:#262626;
    --white:#ffffff;
    --vegan-green:#3f8a2c;
  }
  *{margin:0;padding:0;box-sizing:border-box}
  html,body{width:840px;height:1200px;overflow:hidden}
  body{font-family:"Ubuntu",sans-serif;color:var(--ink);background:var(--wood)}
  .menu{position:relative;width:840px;height:1200px;overflow:hidden;background:var(--wood)}
  .board-line{position:absolute;left:0;width:560px;height:2px;background:var(--wood-line)}
  .abs{position:absolute}

  .brand{position:absolute;left:186px;top:30px;width:200px;text-align:center}
  .brand-dot{width:80px;height:80px;border-radius:50%;background:var(--brand-red);margin:0 auto 26px}
  .brand-name{font-weight:300;font-size:24px;letter-spacing:14px;color:var(--brand-red);padding-left:14px}

  .banner{position:absolute;height:32px;display:flex;align-items:center;justify-content:center}
  .banner svg{position:absolute;inset:0;width:100%;height:100%}
  .banner span{position:relative;font-weight:500;font-size:20px;color:var(--white)}
  .banner small{font-size:15px;font-weight:400}
  .banner--white span{color:var(--brand-red);font-size:24px}

  .persons{position:absolute;left:58px;width:208px;text-align:center;color:var(--price-red);font-size:15px;font-weight:300}
  .item{position:absolute;font-size:12.5px;font-weight:300;line-height:14px;white-space:nowrap}
  .price{position:absolute;font-size:18px;color:var(--price-red);font-weight:400}

  .divider{position:absolute;left:289px;top:254px;width:2px;height:854px;background:var(--brand-red)}

  .set-title{position:absolute;width:120px;text-align:center;font-family:"Stardos Stencil",serif;font-size:21px;color:var(--price-red)}
  .vegan{position:absolute;left:322px;top:1094px;width:200px;text-align:center;font-family:"Stardos Stencil",serif;font-size:21px;color:var(--vegan-green)}
  .allergy{position:absolute;left:300px;top:1128px;width:250px;text-align:center;font-size:10px;font-style:italic;font-weight:300;line-height:13px}

  .dessert-panel{position:absolute;right:0;top:0;width:290px;height:1200px}
  .photo{position:absolute;left:590px;width:208px;height:142px;background:var(--white);padding:7px}
  .photo div{width:100%;height:100%}
  .caption{position:absolute;left:570px;width:250px;text-align:center;color:var(--white);font-size:15px;font-weight:400}
  .dessert-price{position:absolute;left:570px;width:250px;text-align:center;color:var(--white);font-size:24px;font-weight:500}
</style>
</head>
<body>
<main class="menu">
  <div class="board-line" style="top:232px"></div>
  <div class="board-line" style="top:590px"></div>
  <div class="board-line" style="top:816px"></div>
  <div class="board-line" style="top:1044px"></div>

  <svg class="dessert-panel" viewBox="0 0 290 1200" preserveAspectRatio="none" aria-hidden="true">
    <path d="M10 0 L290 0 L290 1200 L18 1200 L14 1120 L20 1040 L12 960 L17 880 L9 800 L16 720 L10 640 L18 560 L11 480 L16 400 L8 320 L15 240 L10 160 L16 80 Z" fill="var(--brand-red)"/>
  </svg>

  <header class="brand">
    <div class="brand-dot"></div>
    <div class="brand-name">MORIVO</div>
  </header>

  <!-- Chef menu -->
  <div class="banner" style="left:58px;top:218px;width:208px">
    <svg viewBox="0 0 260 40" preserveAspectRatio="none" aria-hidden="true"><path d="M8 8 L250 4 L258 12 L248 20 L260 30 L240 36 L12 38 L2 30 L10 22 L0 14 Z" fill="var(--brand-red)"/></svg>
    <span>CHEF MENÜ <small>mit Aperitiv</small></span>
  </div>
  <div class="persons" style="top:256px">für 2 Personen</div>
  <div class="item" style="left:32px;top:283px">Kleine Portion RAMENSUPPE<br>mit Gemüse &amp; Nudeln</div>
  <div class="item" style="left:32px;top:316px">MINI SET</div>
  <div class="item" style="left:32px;top:336px">DESSERT</div>
  <div class="price" style="left:212px;top:310px">81,00€</div>

  <!-- Omakase -->
  <div class="banner" style="left:58px;top:376px;width:208px">
    <svg viewBox="0 0 260 40" preserveAspectRatio="none" aria-hidden="true"><path d="M6 6 L252 5 L256 14 L247 21 L260 29 L244 36 L10 37 L3 28 L11 20 L0 12 Z" fill="var(--brand-red)"/></svg>
    <span>OMAKASE</span>
  </div>
  <div class="persons" style="top:419px">für 2 Personen</div>
  <div class="item" style="left:32px;top:445px">EDAMAME</div>
  <div class="item" style="left:32px;top:465px">OMAKASE SET mit 8<br>Spezialitäten des Hauses</div>
  <div class="item" style="left:32px;top:499px">PANA COTTA mit Beeren</div>
  <div class="price" style="left:213px;top:466px">68,00€</div>

  <!-- Vorspeisen -->
  <div class="banner" style="left:58px;top:547px;width:208px">
    <svg viewBox="0 0 260 40" preserveAspectRatio="none" aria-hidden="true"><path d="M8 7 L250 5 L258 13 L248 21 L259 30 L242 35 L12 37 L2 29 L10 21 L1 13 Z" fill="var(--brand-red)"/></svg>
    <span>VORSPEISEN</span>
  </div>
  <div class="item" style="left:32px;top:612px">MISO SUPPE</div>
  <div class="item" style="left:32px;top:630px">EDAMAME MIT SALZ/CHILI</div>
  <div class="item" style="left:32px;top:648px">SEIDENTOF Uin hausgemachter<br>Sauce mit Mandeln</div>

  <!-- Sushi -->
  <div class="banner" style="left:58px;top:715px;width:208px">
    <svg viewBox="0 0 260 40" preserveAspectRatio="none" aria-hidden="true"><path d="M7 6 L251 5 L257 13 L247 21 L260 30 L242 36 L11 37 L3 29 L10 21 L0 13 Z" fill="var(--brand-red)"/></svg>
    <span>SUSHI</span>
  </div>
  <div class="item" style="left:32px;top:776px">URAMAKI mit Tempuragemüse</div>
  <div class="item" style="left:32px;top:798px">FUTOMAKI wechselndes Gemüse</div>
  <div class="item" style="left:32px;top:821px">URAMAKI mit Austernpilze</div>
  <div class="item" style="left:32px;top:844px">HOSOMAKI Gurke Avocado</div>
  <div class="item" style="left:32px;top:868px">HOSOMAKI Gurke Shiitake</div>
  <div class="item" style="left:32px;top:892px">TOMATEN NIGIRI</div>

  <!-- Kleine Gerichte -->
  <div class="banner" style="left:58px;top:937px;width:208px">
    <svg viewBox="0 0 260 40" preserveAspectRatio="none" aria-hidden="true"><path d="M8 6 L250 5 L258 14 L248 21 L259 30 L243 36 L12 37 L2 29 L10 21 L1 12 Z" fill="var(--brand-red)"/></svg>
    <span>KLEINE GERICHTE</span>
  </div>
  <div class="item" style="left:32px;top:995px">GEMÜSE TEMPURA</div>
  <div class="item" style="left:32px;top:1019px">Crispy TOFUSTICKS mit Mayo</div>
  <div class="item" style="left:32px;top:1043px">KÜRBISKROKETTEN mit TANGASHU</div>
  <div class="item" style="left:32px;top:1067px">SUSHI “THUNA”CAKE</div>
  <div class="item" style="left:32px;top:1091px">SUSHI CAKE CLASSIC</div>
  <div class="item" style="left:32px;top:1115px">AUBERGINE DENGAKU</div>

  <div class="divider"></div>

  <!-- Sets -->
  <div class="set-title" style="left:359px;top:216px">SET 1</div>
  <div class="item" style="left:312px;top:256px">HOSOMAKI</div>
  <div class="item" style="left:312px;top:274px">FUTOMAKI</div>
  <div class="item" style="left:312px;top:293px">NIGIRI</div>
  <div class="item" style="left:312px;top:311px">KÜRBISKROKETTEN</div>
  <div class="item" style="left:312px;top:330px">WAKAME GURKEN SALAT</div>
  <div class="item" style="left:312px;top:348px">PICKLES</div>
  <div class="item" style="left:312px;top:366px">GYOZA TEIGTASCHEN</div>
  <div class="item" style="left:312px;top:385px">SUSHI CAKE</div>
  <div class="price" style="left:484px;top:310px">33,90€</div>

  <div class="set-title" style="left:361px;top:413px">SET 2</div>
  <div class="item" style="left:312px;top:460px">HOSOMAKI</div>
  <div class="item" style="left:312px;top:478px">FUTOMAKI</div>
  <div class="item" style="left:312px;top:497px">PICKLES</div>
  <div class="item" style="left:312px;top:515px">SUSHI “THUNA”CAKE</div>
  <div class="item" style="left:312px;top:534px">Crispy AUBERGINEN mit Mayo</div>
  <div class="item" style="left:312px;top:552px">AUBERGINE DENGAKU</div>
  <div class="price" style="left:484px;top:495px">31,90€</div>

  <div class="set-title" style="left:361px;top:584px">SET 3</div>
  <div class="item" style="left:312px;top:633px">HOSOMAKI</div>
  <div class="item" style="left:312px;top:651px">URAMAKI</div>
  <div class="item" style="left:312px;top:670px">NIGIRI</div>
  <div class="item" style="left:312px;top:688px">GEMÜSE TEMPURA</div>
  <div class="item" style="left:312px;top:706px">CrispyTOFUSTICKS mit Mayo</div>
  <div class="item" style="left:312px;top:724px">WAKAME SHIRA AE</div>
  <div class="price" style="left:484px;top:673px">28,90€</div>

  <!-- Hauptspeisen -->
  <div class="banner" style="left:318px;top:762px;width:206px">
    <svg viewBox="0 0 260 40" preserveAspectRatio="none" aria-hidden="true"><path d="M7 6 L252 5 L257 13 L247 21 L260 30 L243 36 L11 37 L3 29 L10 21 L0 13 Z" fill="var(--brand-red)"/></svg>
    <span>HAUPTSPEISEN</span>
  </div>
  <div class="item" style="left:306px;top:843px;line-height:15px">Herrlich cremiges KATSU CURRY<br>mit knusprigen Auberginensticks,<br>Reis &amp; Pickles</div>
  <div class="item" style="left:306px;top:897px;line-height:15px">RAMEN SUPPE mit Nudeln,<br>Gemüse &amp; Tofu</div>
  <div class="item" style="left:306px;top:936px">CHIRASHI SUSHI BOWL</div>
  <div class="item" style="left:306px;top:959px;line-height:15px">SOMMERSALATE mit Sesamdressing<br>&amp; crispy Tofusticks mit Mayo</div>

  <div class="vegan">ALL VEGAN</div>
  <p class="allergy">Bitte teilen Sie dem Service unbedingt Allergien mit und fragen Sie nach der Allergiker-Menükarte</p>

  <!-- Dessert -->
  <div class="banner banner--white" style="left:590px;top:53px;width:206px">
    <svg viewBox="0 0 260 40" preserveAspectRatio="none" aria-hidden="true"><path d="M6 7 L252 4 L258 13 L249 20 L260 31 L241 36 L10 37 L2 28 L9 21 L0 12 Z" fill="var(--white)"/></svg>
    <span>DESSERT</span>
  </div>

  <div class="photo" style="top:104px"><div role="img" aria-label="Käsekuchen mit roter Beerensauce auf weißem Teller" style="background:linear-gradient(135deg,#f4ead8 0%,#f1dcb5 45%,#c8202a 75%,#f6f1ea 100%)"></div></div>
  <div class="caption" style="top:264px">CHEESECAKE mit Beeren</div>
  <div class="dessert-price" style="top:288px">6,50€</div>

  <div class="photo" style="top:345px"><div role="img" aria-label="Panna Cotta mit Himbeeren in Gläsern auf Holzbrett" style="background:linear-gradient(135deg,#c9d3da 0%,#eceae6 45%,#b0803f 70%,#c8d1d8 100%)"></div></div>
  <div class="caption" style="top:509px">PANACOTTA mit Beeren</div>
  <div class="dessert-price" style="top:533px">5,90€</div>

  <div class="photo" style="top:599px"><div role="img" aria-label="Erdbeersorbet in weißer Schale auf dunklem Tisch" style="background:radial-gradient(circle at 45% 50%,#e8405a 0%,#d7354c 30%,#f1f1f1 45%,#3a2f2a 70%)"></div></div>
  <div class="caption" style="top:763px">SORBET des Tages</div>
  <div class="dessert-price" style="top:789px">5,50€</div>

  <div class="photo" style="top:859px"><div role="img" aria-label="Himbeersorbet mit Schokoladendessert und Minze auf Teller" style="background:radial-gradient(circle at 45% 45%,#c4202e 0%,#a8232a 25%,#eeeeee 55%,#d9d9d9 100%)"></div></div>
  <div class="caption" style="top:1025px">SORBET des Tages mit Schuss</div>
  <div class="dessert-price" style="top:1052px">5,50€</div>
</main>
</body>
</html>
```